New Business Card Design For Re-Branded Company (New Logo)

We recently switched our DBA and had a new logo designed. We now need new business cards made around our new logo. We would like to stick with the color scheme in our logo: White, Orange, and Blue. We want to see original bold designs that reflect our position in the solar energy sector but we prefer simple over complicated.

We are curious about vertical designs so if you can translate your design onto a vertical layout we would be open to look at it. We especially like a few designs we have seen on here that are vertical with a black or very dark gray background. They have our logo on one side and then the normal vertical business card on the other side.

I have included a screenshot of one of the samples we like, labeled sample.jpg and a file we were given as an example of our logo on a dark background.

At the same time we are satisfied to stay with what we have always had in a horizontal format. If it's not a lot of extra work for you, designs that are submitted in both horizontal and vertical formats will be greatly appreciated.

Please submit your original, bold, clean designs for consideration. Contact us with any questions or comments that may arise.

Thank you and Good Luck,

KP

```html
<!DOCTYPE html>
<html lang="en">
<head>
<meta charset="utf-8">
<title>Solara Grid – Business Cards</title>
<link rel="stylesheet" href="https://fonts.googleapis.com/css2?family=Montserrat:wght@600;700&family=Open+Sans:wght@400;600&display=swap">
<style>
  :root {
    --page: #e9e6e1;
    --card-white: #ffffff;
    --black: #050505;
    --blue: #1f6fb5;
    --orange: #e4731f;
    --text-light: #ffffff;
  }
  * { margin: 0; padding: 0; box-sizing: border-box; }
  html, body { width: 1200px; height: 902px; overflow: hidden; }
  body {
    background: var(--page);
    display: flex;
    flex-direction: column;
    align-items: center;
    justify-content: center;
    gap: 50px;
    font-family: "Open Sans", Arial, sans-serif;
  }
  .card {
    position: relative;
    width: 620px;
    height: 354px;
    box-shadow: 0 8px 24px rgba(0,0,0,0.18);
    overflow: hidden;
  }
  /* Back side */
  .card-back { background: var(--card-white); display: flex; align-items: center; justify-content: center; }
  .brand {
    display: flex;
    align-items: center;
    gap: 12px;
    font-family: "Montserrat", Arial, sans-serif;
    font-weight: 700;
    color: var(--orange);
    letter-spacing: 1px;
    white-space: nowrap;
  }
  .brand-dot { border-radius: 50%; background: var(--blue); flex: none; }
  .card-back .brand { font-size: 46px; }
  .card-back .brand-dot { width: 42px; height: 42px; }

  /* Front side */
  .card-front .shapes { position: absolute; inset: 0; }
  .card-front .brand {
    position: absolute;
    left: 28px;
    top: 160px;
    font-size: 23px;
  }
  .card-front .brand-dot { width: 24px; height: 24px; }
  .holder {
    position: absolute;
    right: 26px;
    top: 26px;
    text-align: right;
    color: var(--text-light);
  }
  .holder-name { font-size: 29px; font-weight: 400; letter-spacing: 0.5px; }
  .holder-title { font-size: 17px; margin-top: 2px; }
  .contacts {
    position: absolute;
    right: 20px;
    bottom: 36px;
    list-style: none;
    text-align: right;
    color: var(--text-light);
    font-size: 13.5px;
    line-height: 24px;
  }
  .contacts li { display: flex; justify-content: flex-end; align-items: center; gap: 8px; white-space: nowrap; }
  .contacts .icon {
    width: 14px; height: 14px;
    background: var(--text-light);
    border-radius: 2px;
    display: inline-flex;
    align-items: center;
    justify-content: center;
    flex: none;
  }
</style>
</head>
<body>

  <section class="card card-back" aria-label="Card back">
    <div class="brand"><span class="brand-dot"></span>SOLARA GRID</div>
  </section>

  <section class="card card-front" aria-label="Card front">
    <svg class="shapes" viewBox="0 0 620 354" preserveAspectRatio="none" aria-hidden="true">
      <rect width="620" height="354" fill="var(--blue)"/>
      <path d="M0 0 H272 C305 120 325 240 298 354 H0 Z" fill="var(--orange)"/>
      <path d="M0 0 H238 C280 120 300 240 282 354 H0 Z" fill="var(--card-white)"/>
      <path d="M0 0 H232 C272 120 290 240 268 354 H0 Z" fill="var(--black)"/>
    </svg>

    <div class="brand"><span class="brand-dot"></span>SOLARA GRID</div>

    <div class="holder">
      <div class="holder-name">Owen Harlow</div>
      <div class="holder-title">Founder/CEO</div>
    </div>

    <ul class="contacts">
      <li>555-201-4410
        <span class="icon"><svg width="10" height="10" viewBox="0 0 10 10"><path d="M2 1 L4 1 L4.5 3 L3.5 4 C4 5.5 5 6.5 6 6.5 L7 5.5 L9 6 L9 8 C5 9 1 5 2 1 Z" fill="var(--blue)"/></svg></span></li>
      <li>555-382-7716
        <span class="icon"><svg width="10" height="10" viewBox="0 0 10 10"><rect x="3" y="1" width="4" height="8" rx="1" fill="var(--blue)"/></svg></span></li>
      <li>555-201-4415
        <span class="icon"><svg width="10" height="10" viewBox="0 0 10 10"><rect x="1.5" y="3" width="7" height="5" fill="var(--blue)"/><rect x="3" y="1" width="4" height="2" fill="var(--blue)"/></svg></span></li>
      <li>hello@solaragrid.com
        <span class="icon"><svg width="10" height="10" viewBox="0 0 10 10"><rect x="1" y="2.5" width="8" height="5" fill="none" stroke="var(--blue)" stroke-width="1.2"/><path d="M1 2.5 L5 5.5 L9 2.5" fill="none" stroke="var(--blue)" stroke-width="1.2"/></svg></span></li>
      <li>www.solaragrid.com
        <span class="icon"><svg width="10" height="10" viewBox="0 0 10 10"><circle cx="5" cy="5" r="3.6" fill="none" stroke="var(--blue)" stroke-width="1.2"/><path d="M1.4 5 H8.6" stroke="var(--blue)" stroke-width="1"/></svg></span></li>
      <li class="address">480 Linden Row Fairview TN 37062
        <span class="icon"><svg width="10" height="10" viewBox="0 0 10 10"><path d="M5 9 C3 6.5 2 5 2 3.6 A3 3 0 0 1 8 3.6 C8 5 7 6.5 5 9 Z" fill="var(--blue)"/><circle cx="5" cy="3.6" r="1" fill="var(--text-light)"/></svg></span></li>
    </ul>
  </section>

</body>
</html>
```